7 Loop Flyer

We are a gym named Korvalle and we need a flyer design for our challenge we will be having called the '7 LOOP'. The '7 LOOP' is a 6 Week Transformation Challenge where participants will train throughout the 6 weeks then see what progress they have made at the end, with prizes on offer for the best results.

We would like to see designs that use the colour blue.

The design we would like has been sketched and added in files section, subject to minor word changes later on. Both logos have also been added to the file section as well. As per the sketch, At the top should be the 'Korvalle 7 LOOP' logo. Underneath will have writing that says 'A 6 week transformation challenge that will get you in the best shape of your life!

Below that will say 'NO EGOS REAL PEOPLE REAL RESULTS' underneath each other. With 'ENTRIES NOW OPEN' below.

Then at the bottom the other Korvalle logo.

Colors
33a6d7
85cae6
0292cd
0355a3
3276b5
85abd2
e667a6
e34197

Requirements
Must have
• Mention of the prizes
• "Chance to win over $1200 in prizes"
• 1st Place $600 CASH MONEY!!!!
• Sign up now kicks off September 22
• The ultimate 6 Week Transformation
Should not have
• Generic / Stock images

```html
<!DOCTYPE html>
<html lang="en">
<head>
<meta charset="utf-8">
<title>Korvalle 7 LOOP Flyer</title>
<link rel="stylesheet" href="https://fonts.googleapis.com/css2?family=Anton&family=Roboto+Condensed:wght@300;400&display=swap">
<style>
  :root {
    --page-bg: #e4e4e4;
    --ink: #0a0a0a;
    --paper-white: #ffffff;
    --photo-light: #b9c4d2;
    --photo-mid: #7d8ea6;
    --photo-deep: #4a5a72;
    --band: #000000;
  }
  html, body {
    margin: 0;
    width: 1200px;
    height: 1200px;
    overflow: hidden;
    background: var(--page-bg);
  }
  .flyer {
    position: absolute;
    left: 196px;
    top: 66px;
    width: 808px;
    height: 1044px;
    overflow: hidden;
    font-family: "Roboto Condensed", sans-serif;
    color: var(--ink);
    text-align: center;
  }
  .flyer-photo {
    position: absolute;
    inset: 0;
    background:
      radial-gradient(ellipse 45% 55% at 50% 35%, var(--photo-light) 0%, rgba(185,196,210,0) 70%),
      linear-gradient(180deg, var(--photo-mid) 0%, var(--photo-deep) 100%);
  }
  .line {
    position: absolute;
    left: 0;
    right: 0;
    margin: 0;
    line-height: 1;
    white-space: nowrap;
  }
  .brand-mark {
    position: absolute;
    top: 140px;
    left: 0;
    right: 0;
    display: flex;
    justify-content: center;
    align-items: center;
    gap: 18px;
  }
  .brand-dot {
    width: 34px;
    height: 34px;
    border-radius: 50%;
    background: var(--ink);
  }
  .brand-name {
    font-size: 60px;
    font-weight: 400;
    letter-spacing: 2px;
    line-height: 1;
  }
  .prize-intro { top: 250px; font-size: 30px; font-weight: 400; }
  .prize-first { top: 292px; font-family: "Anton", sans-serif; font-size: 44px; }
  .kickoff { top: 352px; font-size: 28px; font-weight: 400; }
  .headline-lead { top: 432px; font-size: 56px; font-weight: 400; }
  .headline-sub { font-size: 42px; font-weight: 400; }
  .headline-sub.l1 { top: 498px; }
  .headline-sub.l2 { top: 551px; }
  .headline-sub.l3 { top: 602px; }
  .slogan {
    position: absolute;
    left: 0;
    right: 0;
    top: 655px;
    margin: 0;
    font-family: "Anton", sans-serif;
    font-size: 66px;
    line-height: 73px;
    letter-spacing: -1px;
  }
  .entries-band {
    position: absolute;
    left: 0;
    right: 0;
    top: 890px;
    height: 64px;
    background: var(--band);
    color: var(--paper-white);
    font-size: 58px;
    font-weight: 300;
    line-height: 64px;
  }
  .contact {
    top: 966px;
    color: var(--paper-white);
    font-size: 28px;
    font-weight: 400;
  }
  .footer-mark {
    position: absolute;
    top: 1004px;
    left: 0;
    right: 0;
    display: flex;
    justify-content: center;
    align-items: center;
    gap: 10px;
    color: var(--paper-white);
  }
  .footer-dot {
    width: 18px;
    height: 18px;
    border-radius: 50%;
    background: var(--paper-white);
  }
  .footer-name {
    font-size: 28px;
    font-weight: 400;
    letter-spacing: 3px;
    line-height: 1;
  }
</style>
</head>
<body>
  <main class="flyer">
    <div class="flyer-photo" role="img" aria-label="Photo of a muscular athlete gripping a barbell, blue-grey textured backdrop"></div>

    <div class="brand-mark">
      <span class="brand-dot"></span>
      <span class="brand-name">KORVALLE 7 LOOP</span>
    </div>

    <p class="line prize-intro">CHANCE TO WIN OVER $1200 IN PRIZES</p>
    <p class="line prize-first">1ST PLACE $600 CASH MONEY!!!!</p>
    <p class="line kickoff">SIGN UP NOW &middot; KICKS OFF SEPTEMBER 22</p>

    <p class="line headline-lead">A 6 WEEK TRASFORMATION</p>
    <p class="line headline-sub l1">CHALLENGE THAT</p>
    <p class="line headline-sub l2">WILL GET YOU IN THE</p>
    <p class="line headline-sub l3">BEST SHAPE OF YOUR LIFE!</p>

    <p class="slogan">NO EGOS<br>REAL PEOPLE<br>REAL RESULTS</p>

    <div class="entries-band">ENTRIES NOW OPEN</div>
    <p class="line contact">CALL US NOW 155204718&nbsp; OR WWW.THE7LOOP.COM</p>

    <div class="footer-mark">
      <span class="footer-dot"></span>
      <span class="footer-name">KORVALLE</span>
    </div>
  </main>
</body>
</html>
```